Morvadin Nutrition Supplement Jar

Label for jar. White label on a brown bottle jar.
Conservative look, should look like medicine.
Main Side:
Brightfield Health (smaller size) (with logo)
MORVADIN 10mg (large size)
Doctor Formulated
Developed in Clinical Practice
60 Capsules
(I prefer the single color white label with dark brown letters. Please stay close to that design)
(For the back side, please use the multicolor set up)
(The whole Label should be one color - white with dark brown letters)
Please visit my site for more inspiration and feel: www.calmorvex.com
The product will be brown jar listed on this site.
Can you please provide one version without the text "Brightfield Health & Logo".
Thank you.

Target Market(s)

Women, 34-59 years old

Industry/Entity Type

Nutrition

Requirements
Should not have
• Multicolors, leaves,

```html
<!DOCTYPE html>
<html lang="en">
<head>
<meta charset="utf-8">
<title>Morvadin Label</title>
<link href="https://fonts.googleapis.com/css2?family=Rubik:wght@400;500;600;700&display=swap" rel="stylesheet">
<style>
  :root {
    --bg: #ffffff;
    --ink: #2b1a12;
    --ink-soft: #3d2d25;
    --label-light: #ffffff;
    --label-mid: #ececec;
    --label-edge: #d9d9d9;
    --rule: #2b1a12;
  }
  * { margin: 0; padding: 0; box-sizing: border-box; }
  html, body {
    width: 1200px; height: 703px; overflow: hidden;
    background: var(--bg);
    font-family: "Rubik", Arial, sans-serif;
    color: var(--ink);
  }
  .label {
    position: absolute; left: 40px; top: 151px;
    width: 1120px; height: 400px;
    background: linear-gradient(90deg, var(--label-edge) 0%, var(--label-light) 18%, var(--label-mid) 45%, var(--label-light) 62%, var(--label-mid) 85%, var(--label-edge) 100%);
    box-shadow: 0 3px 8px rgba(0,0,0,0.25);
  }
  .facts {
    position: absolute; left: 32px; top: 52px; width: 258px; height: 192px;
    border: 2px solid var(--ink); padding: 4px 8px;
  }
  .facts-title { font-weight: 700; font-size: 15px; }
  .facts-row { display: flex; justify-content: space-between; font-size: 10px; margin-top: 14px; line-height: 1.35; color: var(--ink-soft); }
  .facts-bar { height: 6px; background: var(--ink); margin-top: 6px; }
  .facts-note { font-size: 7.5px; padding: 4px 0 5px; border-bottom: 1px solid #999; color: var(--ink-soft); }
  .facts-list { font-size: 8.6px; line-height: 1.38; margin-top: 6px; color: var(--ink-soft); }
  .maker { position: absolute; left: 33px; top: 270px; color: var(--ink-soft); }
  .maker-line { font-size: 10px; }
  .maker-name { font-size: 17px; font-weight: 700; color: var(--ink); margin-top: 5px; }
  .maker-address { font-size: 10px; line-height: 1.35; margin-top: 14px; }
  .front { position: absolute; left: 415px; top: 44px; width: 300px; }
  .brand { font-size: 40px; font-weight: 700; letter-spacing: 0.5px; line-height: 1; }
  .strength { font-size: 27px; font-weight: 600; margin-top: 4px; }
  .sub { font-size: 14px; margin-top: 8px; }
  .divider { height: 2px; background: var(--rule); width: 300px; margin-top: 26px; }
  .formulated { font-size: 12.5px; font-weight: 600; letter-spacing: 1.2px; margin: 22px 0 0 8px; }
  .claim { font-size: 8.6px; font-weight: 600; line-height: 1.35; width: 210px; margin: 12px 0 0 8px; }
  .developed { font-size: 9px; font-weight: 600; letter-spacing: 0.8px; margin: 32px 0 0 8px; }
  .count { display: flex; align-items: center; gap: 6px; font-size: 12px; margin: 12px 0 0 78px; letter-spacing: 0.5px; }
  .count b { font-weight: 700; }
  .back { position: absolute; left: 791px; top: 52px; width: 290px; font-size: 10.6px; line-height: 1.33; color: var(--ink-soft); }
  .back strong { color: var(--ink); font-weight: 700; }
  .warning { margin-top: 50px; }
  .disclaimer {
    position: absolute; left: 791px; top: 319px; width: 282px; height: 60px;
    border: 1px solid var(--ink); border-radius: 10px;
    padding: 9px 12px; font-size: 8.8px; font-weight: 600; line-height: 1.3; color: var(--ink);
  }
</style>
</head>
<body>
  <div class="label">
    <div class="facts">
      <div class="facts-title">Supplement Facts</div>
      <div class="facts-row"><span>Serving Size:<br>Servings per Container:</span><span>1 capsule&nbsp; 60</span></div>
      <div class="facts-bar"></div>
      <div class="facts-note">Proprietary Formula: 1800 mg (% of Daily Value not Established)</div>
      <div class="facts-list">Thiamin hydrochloride, Riboflavin, Niacinamide, Pyridoxine hydrochloride, Folic Acid, Cyanocobalamin, Biotin, Pueraria Root, Lithium Orotate, Gentian Root, Bupleurum Root, Milk Thistle Seed Extract, Angelica Root, Chanca Piedra, Dandelion Root, Rhodiola Rosea, Saffron.</div>
    </div>

    <div class="maker">
      <div class="maker-line">Manufactured in the USA for</div>
      <div class="maker-name">Calmorvex LLC</div>
      <div class="maker-line">from Globally Sourced Ingredients</div>
      <div class="maker-address">Calmorvex LLC,<br>Aurora, Colorado<br>Ph. 555-010-4821,<br>www.calmorvex.com</div>
    </div>

    <div class="front">
      <div class="brand">MORVADIN</div>
      <div class="strength">10mg</div>
      <div class="sub">CRAVING SUPPORT</div>
      <div class="divider"></div>
      <div class="formulated">DOCTOR FORMULATED</div>
      <div class="claim">In Synergy our ingredients act on Neuro-receptors and Reward System Pathways in the Brain.</div>
      <div class="claim">Reduce cravings and mechanisms of addiction, promote motivation and positive behavior.</div>
      <div class="developed">DEVELOPED THROUGH CLINICAL PRACTICE</div>
      <div class="count">
        <svg width="22" height="9" viewBox="0 0 22 9" aria-hidden="true"><rect x="0.5" y="0.5" width="21" height="8" rx="4" fill="none" stroke="#2b1a12"/><line x1="11" y1="0.5" x2="11" y2="8.5" stroke="#2b1a12"/></svg>
        <span><b>60</b> CAPSULE</span>
      </div>
    </div>

    <div class="back">
      <p><strong>DIRECTIONS:</strong> Take one two capsules after meals. Do not exceed three capsules per day. Take during real time cravings or before drinking situations for additional craving support. Store in a cool dry place, tightly closed. Keep away from children.</p>
      <p class="warning"><strong>WARNING:</strong> Not to be used by children under 18 years, women who are pregnant, may become pregnant, breastfeeding, people taking antidepressant drugs or sedatives. If you are under a physician's care or taking any medications, or being treated for heart disease or diabetes, consult your health care professional before taking this product.</p>
    </div>

    <div class="disclaimer">The FDA has not evaluated these statements. This product is not intended to diagnose, treat, cure, or prevent any disease.</div>
  </div>
</body>
</html>
```